Ma V's -100% Juice -Can Design - 8 Varieties

We are looking for to design our new range of 100% Juices which are made in Vietnam and will be imported into Australia.
Our New Brand is to be called “Ma V’s” or "Ma V's Juices"
We will initially have 8 products in the range. Our range of 100% juices will be packed in 500ml Aluminium Cans.
We envisage to have the same general/consistent branding on each can but with different fruit images of all the different juice varieties to be a main part for the image. I have attached a couple of samples of Juice design so you can use a reference point.
We will have the following varieties in our Juice range:
Pineapple
Mango
Passion fruit
Lychee
Pink Guava
Watermelon
Coconut Water
Coconut Water with Chocolate
We have done a few designs for the branding of "Ma V’s” which are attached below but we are happy if they are modified/adjusted to fit in with the overall design of the can.
The design needs to state:
“100% Natural”
“No Added Sugar”
“Never from Concentrate”
“Made from Whole fruit”
The back of the can will need a Nutritional Panel, Ingredient list and must have a barcode.
Image below attached with requirements needed for Australia.
The cans must look striking so they stand out and elegant and sophisticated.

```html
<!DOCTYPE html>
<html lang="en">
<head>
<meta charset="utf-8">
<title>Ma V's Sparkling Passion Fruit – Can Label</title>
<link rel="stylesheet" href="https://fonts.googleapis.com/css2?family=Cinzel:wght@400;600;700&family=Oswald:wght@300;500&family=Lobster&display=swap">
<style>
  :root {
    --page: #ffffff;
    --gold-light: #f6c35a;
    --gold: #e0a024;
    --gold-deep: #c27c0e;
    --label-white: #f4f2f4;
    --lilac: #e6d3e4;
    --plum: #8a4a7e;
    --plum-mid: #9a5a8e;
    --plum-deep: #5a1f4e;
    --plum-dark: #3a0e32;
    --ink: #3a3a3a;
    --ink-soft: #6e6e6e;
    --fruit-red: #8a2340;
    --fruit-rose: #b8485a;
  }
  * { box-sizing: border-box; margin: 0; padding: 0; }
  html, body { width: 1200px; height: 1200px; overflow: hidden; background: var(--page); }
  .canvas { position: relative; width: 1200px; height: 1200px; }

  .label {
    position: absolute; left: 420px; top: 170px; width: 364px; height: 870px;
    background: linear-gradient(to bottom,
      var(--label-white) 0%, var(--label-white) 58%, var(--lilac) 72%, var(--plum) 88%, var(--plum-deep) 100%);
    overflow: hidden;
  }
  .label::after {
    content: ""; position: absolute; inset: 0;
    background: linear-gradient(to right, rgba(0,0,0,.12) 0%, rgba(255,255,255,0) 18%, rgba(255,255,255,.35) 45%, rgba(255,255,255,0) 70%, rgba(0,0,0,.14) 100%);
    pointer-events: none;
  }

  .brand-band {
    position: absolute; left: 0; top: 0; width: 100%; height: 189px;
    background: linear-gradient(to bottom, var(--gold-deep) 0%, var(--gold) 40%, var(--gold-light) 100%);
    display: flex; align-items: center; justify-content: center;
  }
  .brand-name {
    font-family: "Oswald", sans-serif; font-weight: 500; font-size: 44px;
    color: var(--plum-dark); letter-spacing: 2px; margin-top: 22px;
  }

  .sparkling {
    position: absolute; top: 200px; width: 100%; text-align: center;
    font-family: "Cinzel", serif; font-weight: 600; font-size: 22px; color: var(--ink);
    letter-spacing: 1px;
  }
  .flavour {
    position: absolute; top: 236px; width: 100%; text-align: center;
    font-family: "Lobster", cursive; color: var(--plum-deep); line-height: .86;
  }
  .flavour .line-1 { display: block; font-size: 74px; color: var(--plum-mid); }
  .flavour .line-2 { display: block; font-size: 72px; }
  .descriptor {
    position: absolute; top: 398px; width: 100%; text-align: center;
    font-family: "Cinzel", serif; font-weight: 600; font-size: 27px; color: var(--ink);
    letter-spacing: .5px;
  }
  .descriptor .soft { color: var(--ink-soft); font-weight: 400; }
  .whole-fruit { position: absolute; top: 432px; left: 0; width: 100%; height: 60px; }
  .whole-fruit text { font-family: "Cinzel", serif; font-size: 15px; fill: var(--ink-soft); letter-spacing: 1px; }

  .fruit-visual {
    position: absolute; left: 62px; top: 472px; width: 240px; height: 245px;
    border-radius: 50% 50% 40% 40%;
    background: radial-gradient(ellipse at 50% 55%, var(--fruit-rose) 0%, var(--fruit-red) 45%, rgba(138,35,64,0) 72%);
  }

  .claims {
    position: absolute; top: 724px; width: 100%; text-align: center;
    font-family: "Oswald", sans-serif; font-weight: 300; color: #ffffff; font-size: 19px;
    line-height: 25px; letter-spacing: .3px;
  }
  .claims b { font-weight: 500; }
  .claims .divider { margin: 0 8px; }
  .volume { margin-top: 8px; display: block; }
  .base-band {
    position: absolute; left: 0; bottom: 0; width: 100%; height: 46px; background: var(--plum-dark);
  }
</style>
</head>
<body>
<div class="canvas">
  <div class="label">
    <div class="brand-band"><span class="brand-name">Ma V's</span></div>

    <div class="sparkling">SPARKLING</div>
    <div class="flavour"><span class="line-1">Passion</span><span class="line-2">Fruit</span></div>
    <div class="descriptor"><span class="soft">REAL</span> FRUIT <span class="soft">JUICE</span></div>

    <svg class="whole-fruit" viewBox="0 0 364 60" aria-hidden="true">
      <defs><path id="arc" d="M 60 58 Q 182 0 304 58"/></defs>
      <text><textPath href="#arc" startOffset="50%" text-anchor="middle">MADE WITH WHOLE FRUIT</textPath></text>
    </svg>

    <div class="fruit-visual" role="img" aria-label="Photo of halved passion fruits with a splash of juice"></div>

    <div class="claims">
      <div><b>100%</b> ALL NATURAL<span class="divider">|</span><b>NO</b> ADDED SUGAR</div>
      <div><b>NEVER</b> FROM CONCENTRATE</div>
      <span class="volume">500ml (17 Fl. Oz.)</span>
    </div>
    <div class="base-band"></div>
  </div>
</div>
</body>
</html>
```